TPR Letterhead

We need a letterhead design that will be able to be used on all marketing products (letterhead, mail chimp, envelops, business cards, etc.) We are a law firm specializing primarily in transportation law but offer a wide range of services to our clients. We would like the design to be modern, simple, and professional. Our colors are black and gold, however, we've incorporated dark gray and white on other marketing products such as our website.

```html
<!DOCTYPE html>
<html lang="en">
<head>
<meta charset="utf-8">
<title>TPR Law Group – Stationery</title>
<link href="https://fonts.googleapis.com/css2?family=Cinzel:wght@500&family=Arimo:wght@400&family=Jost:wght@500&display=swap" rel="stylesheet">
<style>
  :root {
    --backdrop: #e9e9e7;
    --paper: #ffffff;
    --ink: #151515;
    --gold: #b08d57;
    --gold-soft: #c9a877;
    --shadow: rgba(0,0,0,0.12);
  }
  * { box-sizing: border-box; margin: 0; padding: 0; }
  html, body { width: 1200px; height: 800px; overflow: hidden; background: var(--backdrop); }
  .canvas { position: relative; width: 1200px; height: 800px; }

  /* Letterhead */
  .letterhead {
    position: absolute; left: 70px; top: 30px; width: 572px; height: 740px;
    background: var(--paper); box-shadow: 0 4px 18px var(--shadow);
    font-family: "Arimo", Arial, sans-serif; color: var(--ink);
  }
  .brand-name {
    font-family: "Cinzel", serif; font-weight: 500; color: var(--ink);
    letter-spacing: 0.06em; line-height: 1;
  }
  .letterhead .brand-name { position: absolute; left: 46px; top: 46px; font-size: 24px; }
  .header-rule { position: absolute; left: 46px; top: 86px; width: 480px; height: 6px; }
  .letter-meta { position: absolute; left: 52px; top: 118px; font-size: 10px; letter-spacing: 0.02em; }
  .letter-meta p + p { margin-top: 22px; }
  .letter-body { position: absolute; left: 52px; top: 182px; width: 470px; font-size: 10px; line-height: 1.45; }
  .letter-body p + p { margin-top: 14px; }

  .contact-list { position: absolute; left: 52px; top: 598px; list-style: none; font-size: 10px; }
  .contact-list li { display: flex; align-items: center; gap: 10px; height: 20px; }
  .contact-list svg { width: 11px; height: 11px; fill: var(--gold); flex: none; }
  .contact-address { display: block; margin-left: 21px; line-height: 1.4; }
  .contact-firm { font-family: "Jost", sans-serif; font-weight: 500; color: var(--gold); font-size: 11px; }
  .footer-band { position: absolute; right: 0; bottom: 44px; width: 270px; height: 26px; }
  .footer-web {
    position: absolute; right: 20px; bottom: 51px; color: var(--paper);
    font-size: 10px; letter-spacing: 0.12em;
  }

  /* Business cards */
  .card {
    position: absolute; width: 420px; height: 240px; background: var(--paper);
    box-shadow: 0 4px 14px var(--shadow);
  }
  .card-back { left: 700px; top: 120px; }
  .card-front { left: 700px; top: 420px; display: flex; align-items: center; justify-content: center; }
  .card-back .brand-name { position: absolute; left: 34px; top: 30px; font-size: 15px; }
  .card-front .brand-name { font-size: 28px; }
  .card-contacts { position: absolute; left: 40px; top: 112px; list-style: none; font-family: "Arimo", Arial, sans-serif; font-size: 9px; color: var(--ink); }
  .card-contacts li { display: flex; align-items: center; gap: 8px; height: 17px; }
  .card-contacts svg { width: 9px; height: 9px; fill: var(--gold); flex: none; }
  .card-contacts .contact-address { margin-left: 17px; }
  .card-contacts .contact-firm { font-size: 10px; }
</style>
</head>
<body>
<main class="canvas">

  <article class="letterhead">
    <div class="brand-name">TPR Law Group</div>
    <svg class="header-rule" viewBox="0 0 480 6" preserveAspectRatio="none" aria-hidden="true">
      <line x1="0" y1="3" x2="480" y2="3" stroke="var(--gold)" stroke-width="2"/>
      <line x1="240" y1="3" x2="480" y2="3" stroke="var(--ink)" stroke-width="2"/>
    </svg>

    <div class="letter-meta">
      <p>SENT VIA EMAIL:</p>
      <p>RE:</p>
    </div>

    <div class="letter-body">
      <p>“Lorem ipsum dolor sit amet, consectetur adipiscing elit, sed do eiusmod tempor incididunt ut labore et dolore magna aliqua. Ut enim ad minim veniam, quis nostrud exercitation ullamco laboris nisi ut aliquip ex ea commodo consequat. Duis aute irure dolor in reprehenderit in voluptate velit esse cillum dolore eu fugiat nulla pariatur. Excepteur sint occaecat cupidatat non proident, sunt in culpa qui officia deserunt mollit anim id est laborum.”</p>
      <p>“Lorem ipsum dolor sit amet, consectetur adipiscing elit, sed do eiusmod tempor incididunt ut labore et dolore magna aliqua. Ut enim ad minim veniam, quis nostrud exercitation ullamco laboris nisi ut aliquip ex ea commodo consequat. Duis aute irure dolor in reprehenderit in voluptate velit esse cillum dolore eu fugiat nulla pariatur. Excepteur sint occaecat cupidatat non proident, sunt in culpa qui officia deserunt mollit anim id est laborum.”</p>
      <p>“Lorem ipsum dolor sit amet, consectetur adipiscing elit, sed do eiusmod tempor incididunt ut labore et dolore magna aliqua. Ut enim ad minim veniam, quis nostrud exercitation ullamco laboris nisi ut aliquip ex ea commodo consequat. Duis aute irure dolor in reprehenderit in voluptate velit esse cillum dolore eu fugiat nulla pariatur. Excepteur sint occaecat cupidatat non proident, sunt in culpa qui officia deserunt mollit anim id est laborum.”</p>
    </div>

    <ul class="contact-list">
      <li><svg viewBox="0 0 24 24" aria-hidden="true"><path d="M6.6 10.8a15.1 15.1 0 0 0 6.6 6.6l2.2-2.2a1 1 0 0 1 1-.25 11.4 11.4 0 0 0 3.6.57 1 1 0 0 1 1 1V20a1 1 0 0 1-1 1A17 17 0 0 1 3 4a1 1 0 0 1 1-1h3.5a1 1 0 0 1 1 1c0 1.25.2 2.45.57 3.57a1 1 0 0 1-.25 1z"/></svg>555.010.2040</li>
      <li><svg viewBox="0 0 24 24" aria-hidden="true"><path d="M2 5h20v14H2z M2 5l10 8 10-8" /></svg>admin@tprlawgroup.com</li>
      <li><svg viewBox="0 0 24 24" aria-hidden="true"><path d="M12 2a10 10 0 1 0 0 20 10 10 0 0 0 0-20zm0 2c1.2 1.5 2 3.6 2.2 7H9.8C10 7.6 10.8 5.5 12 4zm-7.9 7h3.7c.1-2.6.7-4.8 1.6-6.4A8 8 0 0 0 4.1 11zm0 2a8 8 0 0 0 5.3 6.4c-.9-1.6-1.5-3.8-1.6-6.4zm5.7 0c.2 3.4 1 5.5 2.2 7 1.2-1.5 2-3.6 2.2-7zm6.4 0c-.1 2.6-.7 4.8-1.6 6.4a8 8 0 0 0 5.3-6.4zm3.7-2a8 8 0 0 0-5.3-6.4c.9 1.6 1.5 3.8 1.6 6.4z"/></svg>www.tprlawgroup.com</li>
      <li><svg viewBox="0 0 24 24" aria-hidden="true"><path d="M12 2a7 7 0 0 0-7 7c0 5 7 13 7 13s7-8 7-13a7 7 0 0 0-7-7zm0 9.5A2.5 2.5 0 1 1 12 6.5a2.5 2.5 0 0 1 0 5z"/></svg><span class="contact-firm">TPR Law Group</span></li>
      <li><span class="contact-address">220 Harbor View Avenue, Suite 400<br>Coral Bay, FL 33000</span></li>
    </ul>

    <svg class="footer-band" viewBox="0 0 270 26" preserveAspectRatio="none" aria-hidden="true">
      <polygon points="0,26 6,0 12,0 6,26" fill="var(--ink)"/>
      <polygon points="18,26 24,0 270,0 270,26" fill="var(--gold)"/>
    </svg>
    <div class="footer-web">www.tprlawgroup.com</div>
  </article>

  <section class="card card-back">
    <div class="brand-name">TPR Law Group</div>
    <ul class="card-contacts">
      <li><svg viewBox="0 0 24 24" aria-hidden="true"><path d="M6.6 10.8a15.1 15.1 0 0 0 6.6 6.6l2.2-2.2a1 1 0 0 1 1-.25 11.4 11.4 0 0 0 3.6.57 1 1 0 0 1 1 1V20a1 1 0 0 1-1 1A17 17 0 0 1 3 4a1 1 0 0 1 1-1h3.5a1 1 0 0 1 1 1c0 1.25.2 2.45.57 3.57a1 1 0 0 1-.25 1z"/></svg>555.010.2040</li>
      <li><svg viewBox="0 0 24 24" aria-hidden="true"><path d="M2 5h20v14H2z"/></svg>admin@tprlawgroup.com</li>
      <li><svg viewBox="0 0 24 24" aria-hidden="true"><circle cx="12" cy="12" r="10"/></svg>www.tprlawgroup.com</li>
      <li><svg viewBox="0 0 24 24" aria-hidden="true"><path d="M12 2a7 7 0 0 0-7 7c0 5 7 13 7 13s7-8 7-13a7 7 0 0 0-7-7zm0 9.5A2.5 2.5 0 1 1 12 6.5a2.5 2.5 0 0 1 0 5z"/></svg><span class="contact-firm">TPR Law Group</span></li>
      <li><span class="contact-address">220 Harbor View Avenue, Suite 400<br>Coral Bay, FL 33000</span></li>
    </ul>
  </section>

  <section class="card card-front">
    <div class="brand-name">TPR Law Group</div>
  </section>

</main>
</body>
</html>
```